Brightpath - online education agent and consultancy

Online education provider for business to business market needs a dynamic, modern and mobile friendly website. We have the shell view www.quorvane.example but it is boring!
I will need to add courses to the website - Business, Health and Wellbeing, Digital, Aviation.
I am targeting mainly services based industries - so blue collar workers, living in the outer suburbs, will be studying online and most likely from home.
They need to feel safe and secure - we are reputable and importantly can support them all the way to course completion.
What makes us stand out from everyone else - we dont offer any courses - we pick and choose the best courses, with the best providers and only offer quality.
We take the time to find out what the student really wants to achieve and match them with the right education provider.

Target Market(s)

Business to Business - HR managers, People and Culture Managers, employees who are 25+ years currently working wanting to further their careers with accredited qualifications

Industry/Entity Type

Education

Number of Pages Required

5+ page

Font styles to use
Sans Serif

Colors
00a990
acd036
0792cd
a54499
f37122

Requirements
Must have
• Mobile functionality - view on iphone/ipad
• Home page
• Courses section
• Contact us
• Payment checkout to be added
Nice to have
• Fresh, inviting, images that reflect the difference we will make - supporting people through the whole journey.
• It needs to be inviting - homely but modern
Should not have
• Black, dark colours

```html
<!DOCTYPE html>
<html lang="en">
<head>
<meta charset="utf-8">
<title>Quorvane – QvConsult</title>
<link rel="stylesheet" href="https://fonts.googleapis.com/css2?family=Open+Sans:wght@400&family=Raleway:wght@400;500;600&display=swap">
<style>
  :root {
    --green: #acd036;
    --green-light: #c2e05a;
    --green-dark: #8fc21f;
    --blue: #0792cd;
    --orange: #f37122;
    --ink: #1e1e1e;
    --body-text: #555555;
    --phone-text: #3a3a3a;
    --white: #ffffff;
    --rule: #e3e3e3;
  }
  * { margin: 0; padding: 0; box-sizing: border-box; }
  html, body { width: 1200px; height: 1044px; overflow: hidden; background: var(--white); }
  .page { position: relative; width: 1200px; height: 1044px; overflow: hidden; font-family: "Open Sans", sans-serif; }

  .site-header { position: absolute; top: 0; left: 0; width: 1200px; height: 130px; }
  .brand { position: absolute; left: 452px; top: 52px; display: flex; align-items: center; gap: 14px; }
  .brand-name { font-family: "Raleway", sans-serif; font-weight: 400; font-size: 48px; letter-spacing: 3px; color: var(--green-dark); line-height: 1; }
  .brand-dot { width: 18px; height: 18px; border-radius: 50%; background: var(--orange); }
  .phone { position: absolute; left: 911px; top: 82px; display: flex; align-items: center; gap: 6px; }
  .phone-icon { width: 29px; height: 29px; }
  .phone-number { font-family: "Open Sans", sans-serif; font-size: 21px; color: var(--phone-text); letter-spacing: -0.3px; }

  .main-nav { position: absolute; top: 130px; left: 0; width: 1200px; height: 57px; background: linear-gradient(to bottom, var(--green-light), var(--green-dark)); }
  .main-nav a { position: absolute; top: 0; height: 57px; line-height: 57px; text-align: center; color: var(--white); text-decoration: none; font-family: "Raleway", sans-serif; font-weight: 500; font-size: 17.5px; }
  .nav-divider { position: absolute; top: 0; width: 1px; height: 57px; background: rgba(255,255,255,0.45); }

  .hero { position: absolute; top: 187px; left: 0; width: 1200px; height: 299px;
    background: linear-gradient(90deg, #d9cbbd 0%, #e9eef2 14%, #b78a6a 30%, #d8c3b5 48%, #a7b3c9 62%, #c9d2e0 80%, #e5d3b9 100%); }
  .hero-rule { position: absolute; top: 486px; left: 0; width: 1200px; height: 2px; background: var(--rule); }

  .service { position: absolute; top: 548px; left: 140px; width: 615px; }
  .service-title { font-family: "Raleway", sans-serif; font-weight: 400; font-size: 31px; color: var(--ink); letter-spacing: 0.5px; line-height: 1.2; }
  .service p { font-size: 13.4px; line-height: 22.5px; color: var(--body-text); margin-top: 0; }
  .service .lead { margin-top: 18px; }
  .service .second { margin-top: 12px; }
  .service .third { margin-top: 22px; width: 560px; }

  .feature-photo { position: absolute; left: 753px; top: 541px; width: 318px; height: 318px; border-radius: 50%;
    background: radial-gradient(circle at 55% 40%, #f1e3d6 0%, #d7c2ae 40%, #b9b7b4 75%, #9a9fa6 100%); }

  .site-footer { position: absolute; top: 927px; left: 0; width: 1200px; height: 117px; background: var(--blue); }
  .footer-nav a { position: absolute; top: 34px; color: var(--white); text-decoration: none; font-family: "Raleway", sans-serif; font-weight: 500; font-size: 15px; }
  .copyright { position: absolute; left: 138px; top: 65px; font-size: 12.5px; color: var(--white); }
  .social { position: absolute; top: 38px; left: 946px; display: flex; gap: 9px; list-style: none; }
  .social li { width: 21px; height: 21px; border-radius: 50%; background: var(--white); }
</style>
</head>
<body>
<div class="page">
  <header class="site-header">
    <div class="brand">
      <span class="brand-name">QUORVANE</span>
      <span class="brand-dot"></span>
    </div>
    <div class="phone">
      <svg class="phone-icon" viewBox="0 0 30 30" aria-hidden="true">
        <circle cx="15" cy="15" r="15" fill="var(--orange)"/>
        <path d="M10.5 8.5c-1 .8-1.6 2-1 3.8 1.2 3.5 4.2 6.7 7.6 8.1 1.8.7 3.1.1 3.9-.9l.4-.6-2.6-2-1.3 1c-1.8-.8-3.6-2.6-4.4-4.4l1-1.3-2-2.6z" fill="none" stroke="var(--white)" stroke-width="1.6" stroke-linejoin="round"/>
      </svg>
      <span class="phone-number">1300 55 01 99</span>
    </div>
  </header>

  <nav class="main-nav">
    <a href="#" style="left:164px;width:114px;">HOME</a>
    <span class="nav-divider" style="left:278px;"></span>
    <a href="#" style="left:278px;width:199px;">BRIGHTPATH</a>
    <span class="nav-divider" style="left:477px;"></span>
    <a href="#" style="left:477px;width:194px;">OUR COURSES</a>
    <span class="nav-divider" style="left:671px;"></span>
    <a href="#" style="left:671px;width:167px;">LET'S CHAT</a>
    <span class="nav-divider" style="left:838px;"></span>
    <a href="#" style="left:838px;width:198px;">ABOUT QUORVANE</a>
  </nav>

  <div class="hero" role="img" aria-label="Photo of a smiling teacher leaning over to help a student writing at a desk in a bright classroom"></div>
  <div class="hero-rule"></div>

  <section class="service">
    <h1 class="service-title">QVCONSULT</h1>
    <p class="lead">Maribel and her team have over 20+ years experience in General Management, Strategy Development, Operations Management, Financial Modelling and Change Management.&nbsp; With their combined experience in many sectors; IT, FMCG, Government, Tourism and Education the team are able to apply their best practice approach to your business.</p>
    <p class="second">Our team has real experience in establishing and running RTO's for the long term. We work with government assisted programs but prefer to focus on fee for service models.&nbsp; Sustainablity and organic growth are the key to success.</p>
    <p class="third">Compliance.&nbsp; Quality Content. Process and Procedures. Marketing. Systems. Delivery. Student Support. The whole Student Lifecycle.</p>
  </section>

  <div class="feature-photo" role="img" aria-label="Round photo of two smiling women studying together at a computer"></div>

  <footer class="site-footer">
    <nav class="footer-nav">
      <a href="#" style="left:138px;">HOME</a>
      <a href="#" style="left:222px;">BRIGHTPATH</a>
      <a href="#" style="left:373px;">OUR COURSES</a>
      <a href="#" style="left:519px;">LET'S CHAT</a>
      <a href="#" style="left:647px;">ABOUT QUORVANE</a>
    </nav>
    <p class="copyright">© 2016 Company Name&nbsp; All right reserved&nbsp; Term of Use</p>
    <ul class="social" aria-label="Social links">
      <li aria-label="Social link 1"></li>
      <li aria-label="Social link 2"></li>
      <li aria-label="Social link 3"></li>
      <li aria-label="Social link 4"></li>
    </ul>
  </footer>
</div>
</body>
</html>
```